Beautiful Quotes For Social Media Posts

We are looking for 5 beautifully designed quotes for our social media account.

Inspiration of styles we like in both style and color along with a few of our favorite fonts (you are NOT limited to these fonts this is just to give you an idea):
https://morrowstudio.example.net/s/k7p2q9x4m1t8v3n6b5c0z2w8y4j1

*These fonts are property of Morrow Studio. You do not have permission/rights to use them outside of this assignment*

Quotes to use (5):
“Only those who dare to fail greatly can ever achieve greatly.” –Walter J. Simmons
“Don’t go through life, grow through life.” – Neil Ashcombe
“Follow your bliss and the universe will open doors where there were only walls.” – Martin Oakley
“If you don’t like the road you’re walking, start paving another one.” – Greta Vance
“Life is like riding a bicycle. To keep your balance, you must keep moving.” —Oskar Feldmann

File Specifics:
- JPG
- 10x10 in size (square)
- Please include @MorrowStudio in the bottom right left or center of each design

Brand Details:
Soft but rich pastel and bright colors.
Hand Drawn florals, doodles and art
Handwritten looking fonts
Artsy, Creative, Girl and Inspiring

```html
<!DOCTYPE html>
<html lang="en">
<head>
<meta charset="utf-8">
<title>Quote – Only those who dare to fail greatly</title>
<link href="https://fonts.googleapis.com/css2?family=Kaushan+Script&family=Raleway:wght@400;500&display=swap" rel="stylesheet">
<style>
  :root {
    --white: #ffffff;
    --lavender: #e2e6f8;
    --ink: #0d0d0d;
    --gold: #d6bd6c;
    --gold-soft: #e6d49a;
    --handle: #b9a46a;
  }
  html, body {
    margin: 0;
    padding: 0;
    width: 1200px;
    height: 1200px;
    overflow: hidden;
    background: var(--white);
  }
  .quote-card {
    position: relative;
    width: 1200px;
    height: 1200px;
    overflow: hidden;
    background: repeating-linear-gradient(
      135deg,
      var(--lavender) 0px,
      var(--lavender) 64px,
      var(--white) 64px,
      var(--white) 120px
    );
  }
  .quote {
    position: absolute;
    left: 0;
    right: 0;
    top: 365px;
    margin: 0;
    text-align: center;
    font-family: "Kaushan Script", cursive;
    font-weight: 400;
    font-size: 80px;
    line-height: 120px;
    color: var(--ink);
  }
  .quote span { display: block; }
  .attribution {
    position: absolute;
    left: 0;
    right: 0;
    top: 724px;
    margin: 0;
    text-align: center;
    font-family: "Raleway", sans-serif;
    font-weight: 500;
    font-size: 23px;
    color: var(--gold);
  }
  .tree-art {
    position: absolute;
    left: 432px;
    top: 962px;
    width: 336px;
    height: 226px;
    border-radius: 12px;
    background: linear-gradient(180deg, var(--gold-soft), var(--gold));
  }
  .handle {
    position: absolute;
    left: 90px;
    top: 1161px;
    padding: 2px 6px;
    font-family: "Raleway", sans-serif;
    font-weight: 400;
    font-size: 15px;
    color: var(--handle);
    border-left: 1px solid var(--handle);
    border-right: 1px solid var(--handle);
    border-bottom: 1px solid var(--handle);
  }
</style>
</head>
<body>
  <main class="quote-card">
    <blockquote class="quote">
      <span>Only</span>
      <span>those who dare to fail greatly</span>
      <span>can ever achieve greatly</span>
    </blockquote>
    <p class="attribution">Walter J. Simmons</p>
    <div class="tree-art" role="img" aria-label="Three hand-drawn gold scribbled pine trees"></div>
    <div class="handle">@MorrowStudio</div>
  </main>
</body>
</html>
```